Dental Office Needs Exciting New Stationary

We need a stationary design that incorporates the logo that we already have and would like to keep the existing color scheme. We need something clean and professional. This is a Endodontic (root canals) office and must represent a dental specialist's office. I need a design for a business card, envelope, and letterhead that all coordinate. I would like the business card to incorporate the information in the business card sample that I am providing. I made the business card design myself but would like to see a better one.

```html
<!DOCTYPE html>
<html lang="en">
<head>
<meta charset="utf-8">
<title>Summit Endodontics Stationery</title>
<link href="https://fonts.googleapis.com/css2?family=Source+Sans+3:wght@400;600&display=swap" rel="stylesheet">
<style>
  :root {
    --bg: #e9e9eb;
    --paper: #ffffff;
    --brand-blue: #1d6fc0;
    --deep-blue: #2b4aa6;
    --bright-blue: #1f9ad8;
    --band-gray: #7d7f82;
    --text-gray: #4a4a4d;
    --divider: #b9bcc2;
  }
  * { margin: 0; padding: 0; box-sizing: border-box; }
  html, body { width: 1200px; height: 900px; overflow: hidden; }
  body {
    background: var(--bg);
    font-family: "Source Sans 3", Arial, sans-serif;
    color: var(--text-gray);
    position: relative;
  }
  .sheet { position: absolute; background: var(--paper); box-shadow: 0 2px 6px rgba(0,0,0,.25); overflow: hidden; }
  .wordmark { position: absolute; color: var(--brand-blue); font-weight: 600; letter-spacing: .5px; white-space: nowrap; display: flex; align-items: center; }
  .wordmark .dot { display: inline-block; flex: none; border-radius: 50%; background: var(--brand-blue); margin-right: 8px; }
  .contacts { position: absolute; display: flex; line-height: 1.25; }
  .contacts .col + .col { border-left: 1px solid var(--divider); }
  .contacts .label { color: var(--brand-blue); font-weight: 600; }
  .footer-band { position: absolute; left: 0; bottom: 0; width: 100%; }
  .footer-band svg { display: block; width: 100%; height: 100%; }
  .footer-band .web { position: absolute; right: 0; bottom: 0; color: #fff; }

  /* letterhead */
  .letterhead { left: 25px; top: 103px; width: 538px; height: 757px; }
  .letterhead .wordmark { left: 36px; top: 54px; font-size: 22px; }
  .letterhead .wordmark .dot { width: 16px; height: 16px; }
  .letterhead .contacts { left: 36px; top: 683px; font-size: 10px; }
  .letterhead .col { padding-right: 18px; }
  .letterhead .col + .col { padding-left: 18px; }
  .letterhead .footer-band { height: 28px; }
  .letterhead .web { font-size: 10.5px; padding: 0 46px 7px 0; }

  /* business card front */
  .card-front { left: 580px; top: 133px; width: 288px; height: 164px; }
  .card-front .wordmark { left: 64px; top: 30px; font-size: 16px; }
  .card-front .wordmark .dot { width: 12px; height: 12px; }
  .card-front .doctors { position: absolute; left: 0; width: 100%; top: 76px; text-align: center; font-size: 8px; color: var(--brand-blue); font-weight: 600; line-height: 1.3; }
  .card-front .doctors .cred { color: var(--text-gray); font-weight: 400; }
  .card-front .contacts { left: 56px; top: 105px; font-size: 6.5px; }
  .card-front .col:first-child { padding-right: 16px; text-align: right; }
  .card-front .col + .col { padding-left: 16px; }
  .card-front .footer-band { height: 14px; }
  .card-front .web { font-size: 7px; padding: 0 16px 2px 0; }

  /* business card back */
  .card-back { left: 880px; top: 135px; width: 288px; height: 162px; background: linear-gradient(90deg, var(--deep-blue), var(--bright-blue) 55%, var(--deep-blue)); }
  .card-back .wordmark { left: 0; width: 100%; top: 62px; justify-content: center; font-size: 18px; color: #fff; }
  .card-back .wordmark .dot { width: 13px; height: 13px; background: #fff; }
  .card-back .web { position: absolute; left: 0; width: 100%; bottom: 9px; text-align: center; font-size: 7.5px; color: #cfe3f7; }

  /* envelope front */
  .envelope-front { left: 581px; top: 323px; width: 583px; height: 254px; }
  .envelope-front .wordmark { left: 36px; top: 40px; font-size: 22px; }
  .envelope-front .wordmark .dot { width: 16px; height: 16px; }
  .envelope-front .contacts { left: 36px; top: 188px; font-size: 9px; }
  .envelope-front .col { padding-right: 18px; }
  .envelope-front .col + .col { padding-left: 18px; }
  .envelope-front .footer-band { height: 26px; }
  .envelope-front .web { font-size: 10px; padding: 0 30px 6px 0; }

  /* envelope back */
  .envelope-back { left: 581px; top: 600px; width: 581px; height: 252px; background: linear-gradient(90deg, var(--deep-blue), var(--bright-blue) 55%, var(--deep-blue)); }
  .envelope-back svg { position: absolute; inset: 0; width: 100%; height: 100%; }
</style>
</head>
<body>

<section class="sheet letterhead">
  <div class="wordmark"><span class="dot"></span>SUMMIT ENDODONTICS</div>
  <div class="contacts">
    <div class="col">
      <div><span class="label">O</span> : 555.210.4400</div>
      <div><span class="label">F</span> : 555.210.4401</div>
      <div>2480 Birch Street</div>
      <div>Riverton, Ca 95100</div>
    </div>
    <div class="col">
      <div><span class="label">O</span> : 555.318.7700</div>
      <div><span class="label">F</span> : 555.318.7701</div>
      <div>7100 elm ave. Suite #2</div>
      <div>Oakdale, ca 95200</div>
    </div>
  </div>
  <div class="footer-band">
    <svg viewBox="0 0 538 28" preserveAspectRatio="none">
      <rect x="0" y="12" width="300" height="16" fill="var(--band-gray)"/>
      <polygon points="288,28 304,2 538,0 538,28" fill="var(--deep-blue)"/>
      <polygon points="304,2 307,0 538,0" fill="var(--bright-blue)"/>
    </svg>
    <span class="web">www.summitendoclinic.com</span>
  </div>
</section>

<section class="sheet card-front">
  <div class="wordmark"><span class="dot"></span>SUMMIT ENDODONTICS</div>
  <div class="doctors">
    <div>Daniel R Whitford <span class="cred">| DDS MS</span></div>
    <div>Marco T Elvira <span class="cred">| DDS</span></div>
  </div>
  <div class="contacts">
    <div class="col">
      <div><span class="label">O</span> : 555.210.4400</div>
      <div><span class="label">F</span> : 555.210.4401</div>
      <div>2480 Birch Street</div>
      <div>Riverton, Ca 95100</div>
    </div>
    <div class="col">
      <div><span class="label">O</span> : 555.318.7700</div>
      <div><span class="label">F</span> : 555.318.7701</div>
      <div>7100 elm ave. Suite #2</div>
      <div>Oakdale, ca 95200</div>
    </div>
  </div>
  <div class="footer-band">
    <svg viewBox="0 0 288 14" preserveAspectRatio="none">
      <rect x="0" y="6" width="160" height="8" fill="var(--band-gray)"/>
      <polygon points="150,14 158,1 288,0 288,14" fill="var(--deep-blue)"/>
    </svg>
    <span class="web">www.summitendoclinic.com</span>
  </div>
</section>

<section class="sheet card-back">
  <div class="wordmark"><span class="dot"></span>SUMMIT ENDODONTICS</div>
  <div class="web">www.summitendoclinic.com</div>
</section>

<section class="sheet envelope-front">
  <div class="wordmark"><span class="dot"></span>SUMMIT ENDODONTICS</div>
  <div class="contacts">
    <div class="col">
      <div><span class="label">O</span> : 555.210.4400</div>
      <div><span class="label">F</span> : 555.210.4401</div>
      <div>2480 Birch Street</div>
      <div>Riverton, Ca 95100</div>
    </div>
    <div class="col">
      <div><span class="label">O</span> : 555.318.7700</div>
      <div><span class="label">F</span> : 555.318.7701</div>
      <div>7100 elm ave. Suite #2</div>
      <div>Oakdale, ca 95200</div>
    </div>
  </div>
  <div class="footer-band">
    <svg viewBox="0 0 583 26" preserveAspectRatio="none">
      <rect x="0" y="12" width="360" height="14" fill="var(--band-gray)"/>
      <polygon points="346,26 362,2 583,0 583,26" fill="var(--deep-blue)"/>
      <polygon points="362,2 365,0 583,0" fill="var(--bright-blue)"/>
    </svg>
    <span class="web">www.summitendoclinic.com</span>
  </div>
</section>

<section class="sheet envelope-back">
  <svg viewBox="0 0 581 252" preserveAspectRatio="none">
    <path class="flap-line" d="M2,14 L260,100 Q290,112 320,100 L579,14" fill="none" stroke="rgba(10,30,90,.45)" stroke-width="1.5"/>
  </svg>
</section>

</body>
</html>
```